Counselling practice needs a Business Card Design

I need a business card design for a new counselling practice in Canberra, Australia. The name of the practice is Dr Henry Walsh, Counselling Services and the practice focuses on philosophical, narrative and existential counselling for individuals, couples and families. The final design should communicate professionalism, sophistication of analysis and psychological wholeness. The reverse side of the card should have an appointment reminder
Updates

Could the following qualifications also be included on card. BSc (Psychology), BA hons (Philosophy), PhD (Philosophy), Diploma of Community Counselling And the following affiliation Guild of Talk Therapists of Tasvale and District Inc. (GOTTTD) And my contact phone mobile phone number is 0455837190, and email is Henry.Walsh937@mailbrook.example for inclusion as well.

Thank you all who have put in a design so far. I just wanted to clarify some design points based on what you have submitted. 1. The Guild of Talk Therapists. Tasvale and District Inc. (GOTTTD) is an affiliation only. 'Member of the Guild of Talk Therapists. Tasvale and District Inc (GOTTTD)' should appear with the same prominence of a qualification. 2. The Post Graduate Diploma in Community Counselling is a quaification and should appear as 'PG Dip (Community Counselling)' after the other qualifications. 3. I am advertising myself as a counsellor so 'Dr Henry Walsh, Counselling Services' or 'Dr Henry Walsh, Counsellor' is the equivalent of the business name. After looking at some of the designs I prefer Dr Henry Walsh in sentence case rather than all capitals (DR HENRY WALSH). 4. 'Philosophical, narrative and existential counselling for individuals, couples and families' is the description of the type of counselling services and should appear on the card.

One further point. I have updated my email address for the card. It is now drhenrywalsh@tasvaletherapy.example

```html
<!DOCTYPE html>
<html lang="en">
<head>
<meta charset="utf-8">
<title>Dr Henry Walsh – Counselling Services business card</title>
<link rel="stylesheet" href="https://fonts.googleapis.com/css2?family=Roboto+Slab:wght@300;400;700&display=swap">
<style>
  :root {
    --backdrop: #1b1b1c;
    --card: #f6f6f6;
    --ink: #5d6063;
    --ink-soft: #6a6c70;
    --band: #6c6d71;
    --band-text: #f1f1f1;
    --rule: #8a8c90;
  }
  * { margin: 0; padding: 0; box-sizing: border-box; }
  html, body { width: 1200px; height: 1000px; overflow: hidden; }
  body {
    background: var(--backdrop);
    font-family: "Roboto Slab", Georgia, serif;
    color: var(--ink);
    position: relative;
  }
  .card {
    position: absolute;
    left: 259px;
    width: 683px;
    height: 391px;
    background: var(--card);
    overflow: hidden;
  }
  .card--front { top: 75px; }
  .card--back { top: 529px; }

  /* Front */
  .affiliation {
    position: absolute;
    left: 150px;
    top: 120px;
    width: 375px;
    text-align: center;
  }
  .affiliation__name {
    font-weight: 700;
    font-size: 62px;
    line-height: 64px;
    letter-spacing: 4px;
    color: var(--ink);
    border-bottom: 2px solid var(--ink-soft);
    padding-bottom: 2px;
  }
  .affiliation__detail {
    margin-top: 6px;
    font-weight: 300;
    font-size: 19.5px;
    line-height: 24.5px;
    color: var(--ink);
  }
  .affiliation__last {
    display: flex;
    align-items: center;
    gap: 8px;
  }
  .affiliation__last::before,
  .affiliation__last::after {
    content: "";
    flex: 1;
    height: 1px;
    background: var(--ink-soft);
  }

  /* Back */
  .identity {
    position: absolute;
    left: 0;
    right: 0;
    top: 108px;
    text-align: center;
  }
  .identity__title { white-space: nowrap; }
  .identity__name {
    font-weight: 700;
    font-size: 29px;
    color: var(--ink);
  }
  .identity__role {
    font-weight: 300;
    font-size: 19px;
    color: var(--ink);
    border-left: 2px solid var(--ink);
    padding-left: 7px;
    margin-left: 4px;
  }
  .contact {
    margin-top: 4px;
    display: flex;
    justify-content: center;
    align-items: center;
    gap: 22px;
    font-weight: 300;
    font-size: 19px;
    color: var(--ink);
  }
  .contact__item { display: flex; align-items: center; gap: 10px; }
  .contact__icon { width: 20px; height: 16px; fill: var(--ink); }

  .divider {
    position: absolute;
    left: 0; right: 0;
    top: 255px;
    height: 3px;
    background: var(--rule);
  }
  .credentials {
    position: absolute;
    left: 0; right: 0;
    top: 261px;
    bottom: 0;
    background: var(--band);
    color: var(--band-text);
    text-align: center;
    padding-top: 18px;
  }
  .credentials__list {
    list-style: none;
    display: flex;
    justify-content: center;
    gap: 12px;
    font-weight: 700;
    font-size: 19px;
  }
  .credentials__list li + li::before {
    content: "•";
    margin-right: 12px;
  }
  .credentials__focus {
    margin-top: 10px;
    font-weight: 300;
    font-size: 21px;
    line-height: 25px;
  }
  .credentials__focus small {
    display: block;
    font-size: 16.5px;
    line-height: 22px;
  }
</style>
</head>
<body>

<section class="card card--front" aria-label="Card front">
  <div class="affiliation">
    <h1 class="affiliation__name">GOTTTD</h1>
    <p class="affiliation__detail">
      Diploma of Community Counselling And<br>
      the following affiliation Guild of Talk<br>
      Therapists of Tasvale and District
    </p>
    <p class="affiliation__detail affiliation__last"><span>Inc.</span></p>
  </div>
</section>

<section class="card card--back" aria-label="Card back">
  <div class="identity">
    <p class="identity__title">
      <span class="identity__name">Dr Henry Walsh</span><span class="identity__role">COUNSELLING SERVICES</span>
    </p>
    <div class="contact">
      <span class="contact__item">
        <svg class="contact__icon" viewBox="0 0 20 16" aria-hidden="true">
          <path d="M1 5c0-2 4-4 9-4s9 2 9 4v1h-4V4.5C13.5 4 12 3.8 10 3.8S6.5 4 5 4.5V6H1z"/>
          <path d="M6 6h2V5h4v1h2l3 4v5H3v-5z"/>
          <circle cx="10" cy="11" r="2" fill="#f6f6f6"/>
        </svg>
        04.55.83.7190
      </span>
      <span class="contact__item">
        <svg class="contact__icon" viewBox="0 0 20 16" aria-hidden="true">
          <path d="M1 2h18v12H1z"/>
          <path d="M2 3l8 6 8-6" fill="none" stroke="#f6f6f6" stroke-width="1.6"/>
        </svg>
        Henry.Walsh937@mailbrook.example
      </span>
    </div>
  </div>

  <div class="divider"></div>

  <div class="credentials">
    <ul class="credentials__list">
      <li>BSc (Psychology)</li>
      <li>BA hons (Philosophy)</li>
      <li>PhD (Philosophy)</li>
    </ul>
    <p class="credentials__focus">
      Counselling Services and the practice focuses on philosophical
      <small>narrative and existential counselling for individuals, couples and families.</small>
    </p>
  </div>
</section>

</body>
</html>
```